Business card for Medication Therapy Management company
Corvale MTM
Professional
Lionel Fairbrook
PharmD
4873 Wexley St.
Denver, CO
lionel@corvalemtm.com
www.corvalemtm.com
logo attached.... please also see elements of website at www.corvalemtm.com

```html
<!DOCTYPE html>
<html lang="en">
<head>
<meta charset="utf-8">
<title>Corvale MTM – Business Card</title>
<link href="https://fonts.googleapis.com/css2?family=Open+Sans:wght@300;400;600;700&display=swap" rel="stylesheet">
<style>
  :root {
    --page-bg: #e9ebee;
    --navy-dark: #17222c;
    --navy-mid: #2c3e4e;
    --brand-blue: #1f5fa6;
    --brand-red: #c8242b;
    --ink: #3a3f45;
    --ink-soft: #6d737a;
    --card-white: #ffffff;
    --card-grey: #e4e6e8;
    --silver: #b9c1c8;
  }
  * { box-sizing: border-box; margin: 0; padding: 0; }
  html, body {
    width: 1200px; height: 901px; overflow: hidden;
    background: var(--page-bg);
    font-family: "Open Sans", Arial, sans-serif;
  }
  .stage {
    position: relative; width: 1200px; height: 901px;
  }
  .card {
    position: absolute; left: 250px; width: 700px; height: 400px;
    border-radius: 22px; overflow: hidden;
    box-shadow: 0 10px 30px rgba(0,0,0,.18);
  }

  /* Back side */
  .card-back {
    top: 34px;
    background: radial-gradient(ellipse at 55% 40%, var(--navy-mid) 0%, var(--navy-dark) 75%);
  }
  .card-back .wordmark {
    position: absolute; left: 0; right: 0; top: 160px;
    display: flex; justify-content: center; align-items: center; gap: 14px;
  }
  .card-back .wordmark-text {
    font-weight: 300; font-size: 44px; letter-spacing: 3px;
    color: var(--silver); text-transform: uppercase;
  }
  .card-back .wordmark-dot {
    width: 26px; height: 26px; border-radius: 50%; background: var(--silver);
  }
  .card-back .web {
    position: absolute; left: 0; right: 0; top: 232px; text-align: center;
    font-size: 14px; letter-spacing: 5px; color: #7f8c97;
  }

  /* Front side */
  .card-front {
    top: 467px;
    background: linear-gradient(180deg, var(--card-white) 0%, #f6f7f8 70%, var(--card-grey) 100%);
  }
  .logo-block {
    position: absolute; left: 40px; top: 138px; width: 300px;
  }
  .logo-block .wordmark {
    display: flex; align-items: center; gap: 10px;
  }
  .logo-block .wordmark-text {
    font-weight: 300; font-size: 36px; letter-spacing: 1.5px;
    color: var(--ink); text-transform: uppercase; white-space: nowrap;
  }
  .logo-block .wordmark-dot {
    width: 20px; height: 20px; border-radius: 50%; background: var(--brand-red);
  }
  .logo-block .tagline {
    margin-top: 4px; font-size: 12.5px; font-weight: 600; letter-spacing: 1.2px;
    color: var(--ink); text-transform: uppercase;
  }
  .divider {
    position: absolute; left: 360px; top: 80px; width: 1px; height: 210px;
    background: linear-gradient(180deg, transparent, #b8bdc2 20%, #b8bdc2 80%, transparent);
  }
  .contact {
    position: absolute; left: 385px; top: 96px; color: var(--ink);
  }
  .contact .name {
    font-size: 26px; font-weight: 600; color: var(--brand-blue); line-height: 1.1;
  }
  .contact .title {
    font-size: 15px; color: var(--ink-soft); margin-top: 4px;
  }
  .contact .address {
    margin-top: 38px; font-size: 14px; line-height: 1.4;
  }
  .contact .lines { margin-top: 18px; list-style: none; }
  .contact .lines li {
    display: flex; align-items: center; gap: 9px; font-size: 14px; line-height: 1.45;
  }
  .contact .lines svg { width: 13px; height: 13px; flex: none; }
  .stripe-blue {
    position: absolute; left: 0; right: 0; top: 328px; height: 4px; background: var(--brand-blue);
  }
  .footer-band {
    position: absolute; left: 0; right: 0; top: 332px; height: 50px;
    display: flex; align-items: center; padding-left: 150px;
    font-size: 14px; letter-spacing: 5px; color: var(--ink-soft);
  }
  .stripe-red {
    position: absolute; left: 0; right: 0; top: 382px; height: 5px; background: var(--brand-red);
  }
</style>
</head>
<body>
<main class="stage">

  <section class="card card-back" aria-label="Card back">
    <div class="wordmark">
      <span class="wordmark-text">Corvale MTM</span>
      <span class="wordmark-dot"></span>
    </div>
    <p class="web">www.corvalemtm.com</p>
  </section>

  <section class="card card-front" aria-label="Card front">
    <div class="logo-block">
      <div class="wordmark">
        <span class="wordmark-text">Corvale MTM</span>
        <span class="wordmark-dot"></span>
      </div>
      <p class="tagline">Medication Therapy Management</p>
    </div>

    <div class="divider"></div>

    <div class="contact">
      <h1 class="name">Lionel Fairbrook</h1>
      <p class="title">PharmD</p>
      <p class="address">4873 Wexley St.<br>Denver, CO<br>80214</p>
      <ul class="lines">
        <li>
          <svg viewBox="0 0 16 16"><rect width="16" height="16" rx="2" fill="#c8242b"/><path d="M4 4h3l1 2.5-1.5 1a6 6 0 0 0 2 2l1-1.5L12 9v3a1 1 0 0 1-1 1C7 13 3 9 3 5a1 1 0 0 1 1-1z" fill="#fff"/></svg>
          303-555-0147
        </li>
        <li>
          <svg viewBox="0 0 16 16"><rect width="16" height="16" rx="2" fill="#c8242b"/><path d="M4 4h3l1 2.5-1.5 1a6 6 0 0 0 2 2l1-1.5L12 9v3a1 1 0 0 1-1 1C7 13 3 9 3 5a1 1 0 0 1 1-1z" fill="#fff"/></svg>
          855-555-0182
        </li>
        <li>
          <svg viewBox="0 0 16 16"><rect width="16" height="16" rx="2" fill="#c8242b"/><rect x="3" y="4.5" width="10" height="7" fill="none" stroke="#fff" stroke-width="1.3"/><path d="M3 4.5l5 4 5-4" fill="none" stroke="#fff" stroke-width="1.3"/></svg>
          lionel@corvalemtm.com
        </li>
      </ul>
    </div>

    <div class="stripe-blue"></div>
    <div class="footer-band">www.corvalemtm.com</div>
    <div class="stripe-red"></div>
  </section>

</main>
</body>
</html>
```